Create a small A5 sized booklet out of a few Word files

The booklet contains instructions for patients who have had surgery. There are about six A4 pages of text which need to be re-formatted and designed into an A5 sized booklet. And a simple front cover for the booklet that says something like "Calloway Centre for Bariatric Surgery. Post operative instructions for bariatric patients"

```html
<!DOCTYPE html>
<html lang="en">
<head>
<meta charset="utf-8">
<title>Calloway Centre for Bariatric Surgery – Post operative booklet</title>
<link rel="stylesheet" href="https://fonts.googleapis.com/css2?family=Arimo:ital,wght@0,400;0,700;1,400;1,700&family=Tinos:wght@400;700&display=swap">
<style>
:root{
  --bg:#a0a1a3;
  --paper:#ffffff;
  --green:#3f7766;
  --green-light:#dde5e1;
  --grey:#7f8183;
  --grey-cover:#b6b7b9;
  --ink:#231f20;
  --rule:#b9bcbb;
}
*{box-sizing:border-box;margin:0;padding:0}
html,body{width:1200px;height:2880px;overflow:hidden;background:var(--bg)}
body{position:relative;font-family:"Arimo",Arial,sans-serif;color:var(--ink)}
.version-label{position:absolute;left:820px;top:36px;font:700 31px "Arimo",Arial,sans-serif;color:#fff}

.page{position:absolute;width:354px;height:503px;background:var(--paper);overflow:hidden}
.col-l{left:224px}.col-r{left:621px}
.row-1{top:643px}.row-2{top:1192px}.row-3{top:1736px}.row-4{top:2283px}

/* cover */
.cover{left:621px;top:93px}
.cover-base{position:absolute;left:0;right:0;top:264px;bottom:0;background:var(--grey-cover)}
.cover-brand{position:absolute;left:0;right:0;top:28px;display:flex;justify-content:center;align-items:center;gap:6px}
.cover-brand .mark{width:30px;height:30px;background:var(--green)}
.cover-brand .name{font:400 13px/1.05 "Tinos",serif;color:var(--green);width:150px}
.cover-title{position:absolute;left:0;right:0;top:176px;text-align:center;font:400 32px/1.02 "Tinos",serif;color:var(--ink)}
.cover-tag{position:absolute;left:87px;width:180px;top:250px;height:34px;background:var(--green);color:#fff;text-align:center;font:700 11px/1.1 "Arimo",sans-serif;padding-top:5px}

/* inner pages */
.page-head{position:absolute;left:36px;right:35px;top:18px;height:38px;border-bottom:1px solid var(--rule);display:flex;justify-content:space-between}
.brand{display:flex;gap:4px;align-items:flex-start}
.brand .mark{width:22px;height:22px;background:var(--green)}
.brand .name{font:400 8px/1.05 "Tinos",serif;color:var(--green);width:92px;padding-top:3px}
.surgeon{font:400 4.6px/1.25 "Arimo",sans-serif;text-align:right;color:var(--grey);padding-top:8px}
.surgeon b{color:var(--green)}
.body{position:absolute;left:36px;right:35px;top:74px;bottom:30px;font-size:7.3px;line-height:1.13;text-align:justify;overflow:hidden}
.body.drop{top:112px}
.page-title{text-align:center;color:var(--green);font-weight:700;font-size:11px;line-height:1.2;margin:2px 0 10px}
.section-title{text-align:center;color:var(--green);font-weight:700;font-size:11px;margin:8px 0 4px}
.sub{color:var(--green);font-weight:700;font-style:italic;margin-top:5px}
.body p{margin-bottom:1px}
.gap{margin-bottom:6px!important}
ul.arrows,ul.dots{list-style:none;margin:3px 0 4px 14px}
ul.arrows li,ul.dots li{position:relative;padding-left:10px;margin-bottom:1.5px}
ul.arrows li::before{content:"➢";position:absolute;left:0;font-size:6.5px}
ul.dots li::before{content:"";position:absolute;left:1px;top:2.5px;width:3px;height:3px;border-radius:50%;background:var(--ink)}
ul.tight{margin-left:6px}
ul.nested{margin:1px 0 2px 6px}
.center{text-align:center}
.strong{font-weight:700}

.schedule{width:100%;border-collapse:collapse;font-size:6.4px;line-height:1.1;margin-top:4px;text-align:left}
.schedule th{background:var(--green);color:#fff;font-weight:700;padding:3px 3px;text-align:center;border:1px solid #fff}
.schedule td{padding:2.5px 3px;border:1px solid #fff;border-bottom:1px solid #cfd6d3;vertical-align:top}
.schedule tr:nth-child(even) td{background:var(--green-light)}
.schedule td:nth-child(2){text-align:center;font-weight:700;width:62px}
.schedule td:nth-child(3){font-style:italic;width:110px}
.schedule-label{text-align:center;font-weight:700;text-decoration:underline;margin-top:8px}

.page-foot{position:absolute;left:0;right:0;bottom:0;height:25px;background:var(--green);display:flex;align-items:center;color:#fff;font-size:5px}
.page-foot .num{width:34px;height:25px;background:var(--grey);display:flex;align-items:center;justify-content:center;font-weight:700;font-size:7.5px}
.page-foot .text{padding:0 12px}
.page-foot.right{justify-content:flex-end}
.alarm{float:right;width:56px;height:26px;margin:0 0 2px 6px}
</style>
</head>
<body>

<div class="version-label">Version_02</div>

<!-- Cover -->
<section class="page cover">
  <div class="cover-base"></div>
  <div class="cover-brand"><span class="mark"></span><span class="name">Calloway Centre for Bariatric Surgery</span></div>
  <h1 class="cover-title">Calloway Centre<br>for Bariatric Surgery</h1>
  <div class="cover-tag">Post operative instructions<br>for bariatric patients</div>
</section>

<!-- Page 2 -->
<section class="page col-l row-1">
  <header class="page-head"><div class="brand"><span class="mark"></span><span class="name">Calloway Centre for Bariatric Surgery</span></div><div class="surgeon"><b>Mr Adrian Calder MBBS FRACS GradCert</b><br>Bariatric, Upper GI &amp; General Surgeon</div></header>
  <div class="body">
    <h2 class="page-title">DISCHARGE INFORMATION<br>Introduction &amp; Appointment Schedule</h2>
    <p class="gap">Congratulations on the commencement of your weight loss journey! Enclosed are some small items and information that will help you manage the first stages of your recovery. From all of us at CCBS we wish you the very best of good fortune and a smooth recovery ongoing!</p>
    <p class="center strong">Standard Appointment Schedule first 12 months.</p>
    <ul class="arrows">
      <li>Variations on this will depend on your individual progress and needs.</li>
      <li>Please note – unless you have pre-arranged your first post op surgeon’s appointment you will need to call or email the rooms after discharge to organise this appointment.</li>
    </ul>
    <p class="schedule-label">Schedule</p>
    <table class="schedule">
      <tr><th>Event</th><th>Time Post op</th><th>Comment</th></tr>
      <tr><td>Phone call from dietician</td><td>1-2 weeks</td><td></td></tr>
      <tr><td>Post op appointment with surgeon</td><td>2 weeks</td><td>Timing may vary according to availability of local consulting</td></tr>
      <tr><td>Second appointment with dietician</td><td>3 months</td><td>May vary depending on your dietician</td></tr>
      <tr><td>Second appointment with surgeon</td><td>3 months</td><td></td></tr>
      <tr><td>First nutritional screen (blood test) sent out (SIPS patients only)</td><td>3 months</td><td>SIPS patients only. Aim to complete blood test prior to surgeon’s appointment</td></tr>
      <tr><td>First nutritional screen sent out(all other patients)</td><td>6 months</td><td>Except SIPS patients – this will be their 2nd screen</td></tr>
      <tr><td>Third appointment with dietician</td><td>6 months</td><td>Dependent on discussions with your dietician</td></tr>
      <tr><td>Second nutritional screen sent out</td><td>12 months</td><td>Ideally have the screen done prior to your 12 month surgical review</td></tr>
      <tr><td>Third appointment with surgeon</td><td>12 months</td><td></td></tr>
    </table>
  </div>
  <footer class="page-foot"><span class="num">2</span><span class="text"><b>Calloway Centre for Bariatric Surgery.</b> Post operative instructions for bariatric patients</span></footer>
</section>

<!-- Page 3 -->
<section class="page col-r row-1">
  <header class="page-head"><div class="brand"><span class="mark"></span><span class="name">Calloway Centre for Bariatric Surgery</span></div><div class="surgeon"><b>Mr Adrian Calder MBBS FRACS GradCert</b><br>Bariatric, Upper GI &amp; General Surgeon</div></header>
  <div class="body">
    <h2 class="page-title">DISCHARGE INFORMATION<br>Basics of the post operative diet</h2>
    <p class="gap">Dietary phases should be comprehensively covered by your pre and post surgery dietician consultations. The following represents only a brief overview to focus your attention on the key points. For further details and discussion please contact your dietician for advice or access your written resources.</p>
    <p class="gap">I would encourage you not to over-think your food decisions and behaviours too much. Worrying too much about every gram of protein or every drink/texture will only lead to severe anxiety setting in!</p>
    <p class="strong">These basic rules apply to most patients after bariatric procedures:</p>
    <ul class="dots tight strong">
      <li>Two weeks liquid diet (thin liquids) – <i style="font-weight:400">followed by…</i></li>
      <li>Two weeks pureed/mashed type foods – <i style="font-weight:400">followed by…</i></li>
      <li>Slow introduction of normal solid foods starting with easier textures</li>
    </ul>
    <p class="strong" style="margin-top:6px">Key points</p>
    <ul class="arrows">
      <li>Liquids, purees, solids should be <u>nourishing</u>. i.e. not just water or cordial or juice etc.</li>
      <li>Go slowly, stop if you feel full or about to vomit</li>
      <li>You will need to work hard to hydrate yourself properly in the early stages – keep sipping away throughout the day</li>
      <li>Avoid gulps of liquids with solid meals. Separate drinking from eating by about 30 minutes before and after. Catch up on hydration in between solid meals.</li>
      <li>Sitting up makes it easier to get liquid and food down</li>
      <li>For solid foods, half a cup is usually sufficient in the first few months</li>
      <li>Don’t keep picking away at your meal for more than 10 minutes – this should be as much time as necessary to complete a meal.</li>
      <li>Ensure you have a high component of protein in your diet</li>
      <li>Start your vitamins usually within two weeks of surgery, as discussed with your dietician</li>
      <li>If you are not tolerating your vitamins, make contact with your dietician to discuss alternatives</li>
    </ul>
  </div>
  <footer class="page-foot right"><span class="text"><b>Calloway Centre for Bariatric Surgery.</b> Post operative instructions for bariatric patients</span><span class="num">3</span></footer>
</section>

<!-- Page 4 -->
<section class="page col-l row-2">
  <header class="page-head"><div class="brand"><span class="mark"></span><span class="name">Calloway Centre for Bariatric Surgery</span></div><div class="surgeon"><b>Mr Adrian Calder MBBS FRACS GradCert</b><br>Bariatric, Upper GI &amp; General Surgeon</div></header>
  <div class="body">
    <h2 class="page-title">General Information and Frequently<br>Asked Questions</h2>
    <p class="sub">General Advice</p>
    <p>You should be mobile and on your feet from the day of discharge. Apart from general recovery this will help prevent clots forming in your legs (deep venous thrombosis)</p>
    <p class="sub">Work</p>
    <p>Most people will be fine to return to work after two weeks. Some with office jobs or home based work may prefer to go back after one week or even earlier. Physically demanding jobs where heavy lifting or strenuous activity is required should only be recommenced after four weeks unless light duties can be allocated</p>
    <p class="sub">Walking</p>
    <p>You can go walking outside the house as soon as you feel comfortable. Aim to increase the amount of walking progressively over the weeks after your surgery</p>
    <p class="sub">Swimming</p>
    <p>Swimming is fine one week post surgery as long as you have well attached, waterproof dressings. After the dressings have been removed, swimming is ok as long as all the wounds are nicely sealed and no longer gaping</p>
    <p class="sub">Gym</p>
    <p>Cardio exercises like running, power walking, step machine etc. are fine from two weeks post surgery. Lifting weights should not occur until at least four weeks</p>
    <p class="sub">Driving</p>
    <p>You can drive a car 5 days after surgery as long as your pain levels are under control and you are no longer requiring strong or sedative pain killers</p>
    <p class="sub">Lifting</p>
    <p>Heavy lifting should be avoided until 4 weeks post surgery. Avoid lifting 10kg or more during this time if practical. Lifting small children is sometimes unavoidable however find other alternatives where possible. Strenuous pushing and pulling activities should be treated similarly</p>
  </div>
  <footer class="page-foot"><span class="num">4</span><span class="text"><b>Calloway Centre for Bariatric Surgery.</b> Post operative instructions for bariatric patients</span></footer>
</section>

<!-- Page 5 -->
<section class="page col-r row-2">
  <header class="page-head"><div class="brand"><span class="mark"></span><span class="name">Calloway Centre for Bariatric Surgery</span></div><div class="surgeon"><b>Mr Adrian Calder MBBS FRACS GradCert</b><br>Bariatric, Upper GI &amp; General Surgeon</div></header>
  <div class="body drop">
    <p class="sub" style="margin-top:0">Anti-inflammatories</p>
    <p>This class of drugs (NSAIDS) include things like Ibuprofen, Dicloven, Celexib, Meloxicam and others. These medications can irritate the stomach and bowel and in some cases cause ulceration. Ideally they are to be avoided in the first 6 weeks after surgery to encourage healing of the tissues. If required regularly and ongoing in most cases it is best to take a low dose anti-acid tablet as well such as Pantorex or Esomax 20mg daily to protect the stomach and bowel lining. This is particularly important in gastric bypass surgery.</p>
    <p class="sub">Alcohol</p>
    <p>Avoiding alcohol for six weeks after surgery is sensible whilst the surgery is healing. Going forward be mindful that alcohol will affect you more quickly and its effects may be stronger after having bariatric surgery. If you are driving be aware that your blood alcohol level may rise faster with less standard drinks than with a normal stomach.</p>
    <p class="sub">Sex</p>
    <p>A common sense approach should be taken with respect to sexual activity. After four weeks there are no specific restrictions on any activities. With care sexual activity could potentially resume earlier as long as you feel comfortable and pain free</p>
    <h3 class="section-title">Wounds</h3>
    <p class="sub" style="margin-top:0">Dressings</p>
    <p>The dressings should be waterproof and allow you to shower. If the dressings are tatty, dirty or blood-soaked in the first ten days you can change one or more dressings with the replacements provided. Note that if you have had a drain tube after surgery, that particular wound where the drain has been tends to take longer to seal properly and may require dressings for a full two weeks. Dressings can otherwise be removed (by anyone including yourself) after 10 days or you can wait until your post-operative appointment. Past 14 days it is advisable to remove the dressings as they are usually getting a bit mucky by this stage. Underneath as long as the wounds are sealed you can shower as per normal</p>
  </div>
  <footer class="page-foot right"><span class="text"><b>Calloway Centre for Bariatric Surgery.</b> Post operative instructions for bariatric patients</span><span class="num">5</span></footer>
</section>

<!-- Page 6 -->
<section class="page col-l row-3">
  <header class="page-head"><div class="brand"><span class="mark"></span><span class="name">Calloway Centre for Bariatric Surgery</span></div><div class="surgeon"><b>Mr Adrian Calder MBBS FRACS GradCert</b><br>Bariatric, Upper GI &amp; General Surgeon</div></header>
  <div class="body">
    <p class="sub" style="margin-top:0">Lumps, Threads</p>
    <p>Lumpiness/firmness under the wound is typical and will resolve over several weeks. If you see suture thread sticking up from a corner of the wound it may need to be removed. Your doctor can do this or if you are feeling brave, pick up the thread with tweezers, pull as much out as you can then cut it off at skin level</p>
    <p class="sub">Discomfort, pain</p>
    <p>It is normal to experience some discomfort, pain or pulling related to one or more wounds either at skin level or deeper. Discomfort should improve with time</p>
    <p class="sub">Redness, smelliness, pus</p>
    <p>These are signs of possible wound infection. You should organise to be seen by your GP or surgeon and a short antibiotic course may be necessary</p>
    <p class="sub">Allergy, intolerance to dressings</p>
    <p>Many patients have minor allergies or intolerances to dressings. If the skin becomes excessively itchy or red underneath the whole extent of the dressing it is best simply to remove the dressing and leave the wound uncovered</p>
    <h3 class="section-title">Symptoms</h3>
    <p class="sub" style="margin-top:0">Pain</p>
    <p>If you have been discharged from hospital, your pain levels should be well manageable with oral tablets. For most patients paracetamol is the basis of pain relief and can be taken regularly every 6 hours. If necessary stronger pain relievers can be taken additionally and are typically chosen by your anaesthetist (e.g. Oxydone, Tapenta). If your pain and discomfort is manageable it is preferrable to reduce or avoid these stronger tablets as they can contribute to nausea, constipation and general immobility.</p>
    <p class="sub">Nausea</p>
    <p>If you are suffering nausea transiently or ongoing, be reassured that this will settle with time! You should have been prescribed anti-nausea medications such as Ondansetron/Ondazen which you should take as recommended for as long as you need to. Keep track of your fluid intake over the day and how you are feeling generally. If you are tolerating very little fluid (e.g. less than 500ml in 24 hours) and are feeling very flat then contact your surgeon. If you are vomiting persistently over the day without relief you should also contact your surgeon.</p>
  </div>
  <footer class="page-foot"><span class="num">6</span><span class="text"><b>Calloway Centre for Bariatric Surgery.</b> Post operative instructions for bariatric patients</span></footer>
</section>

<!-- Page 7 -->
<section class="page col-r row-3">
  <header class="page-head"><div class="brand"><span class="mark"></span><span class="name">Calloway Centre for Bariatric Surgery</span></div><div class="surgeon"><b>Mr Adrian Calder MBBS FRACS GradCert</b><br>Bariatric, Upper GI &amp; General Surgeon</div></header>
  <div class="body">
    <p class="sub" style="margin-top:0">Reflux</p>
    <p>Reflux symptoms may be in the form of “heartburn” (a rising burning sensation behind the middle of your chest) or acid or bile coming up into your mouth or the back of your throat. Reflux can sometimes be caused or exacerbated by bariatric procedures. The symptoms may be transient or occasionally ongoing. Sometimes certain foods can be triggers for reflux or perhaps overeating. In the absence of excessive vomiting or food regurgitation it is unlikely there is any serious anatomical issue underlying. At night it may help to sleep propped up on two or more pillows. Antacids such as Antacel, Refluxa, Chewze etc. can be useful in mild cases. For ongoing significant symptoms a more powerful medication such as Pantorex (pantoprazole) or Esomax (esomeprazole) can be very helpful. Low dose Pantorex or Esomax can be obtained from your chemist without prescription. For higher doses or ongoing requirements seek prescription from your GP or specialist. For more severe intractable cases of reflux where medication is not sufficient further investigation may be warranted and corrective surgery may be possible.</p>
    <p class="sub">Gas</p>
    <p>It is a common experience after most bariatric procedures that burping or gas related symptoms can arise. This may be best explained by the fact that the large reservoir of the stomach is no longer able to store gas for periods of time before expelling it. Hence the gas sometimes tends to move wherever it likes! For some people excessive air swallowing during eating, drinking or speaking can exacerbate the problem. There is no easy solution for excessive gas – you can try Ease-Gas medication from the Chemist which may help. For most people these symptoms will settle with time.</p>
    <p class="sub">Constipation</p>
    <p>Reduced intake, dehydration and taking strong pain killers can predispose patients to constipation in the early weeks after surgery. Keeping up with fluid intake and ensuring some fruits and vegetables are part of your diet is the first step. A fibre supplement taken at least twice a day (e.g. Fibrelle) can help as can Lactulose syrup. Both of these can be purchased over the counter from your chemist. If you are experiencing ongoing pain or problems related to constipation try a Minilax enema.</p>
  </div>
  <footer class="page-foot right"><span class="text"><b>Calloway Centre for Bariatric Surgery.</b> Post operative instructions for bariatric patients</span><span class="num">7</span></footer>
</section>

<!-- Page 8 -->
<section class="page col-l row-4">
  <header class="page-head"><div class="brand"><span class="mark"></span><span class="name">Calloway Centre for Bariatric Surgery</span></div><div class="surgeon"><b>Mr Adrian Calder MBBS FRACS GradCert</b><br>Bariatric, Upper GI &amp; General Surgeon</div></header>
  <div class="body" style="top:80px">
    <h2 class="page-title">DISCHARGE INFORMATION<br>Complications, Red Flags and Contacts</h2>
    <svg class="alarm" viewBox="0 0 56 26" role="img" aria-label="Two warning light icons">
      <g fill="none" stroke="#555" stroke-width="1">
        <path d="M6 22 V14 a6 6 0 0 1 12 0 V22 Z"/><rect x="4" y="22" width="16" height="3"/>
        <path d="M12 2 v4 M3 6 l3 3 M21 6 l-3 3 M1 13 h3 M20 13 h3"/>
      </g>
      <g>
        <path d="M36 22 V14 a6 6 0 0 1 12 0 V22 Z" fill="#555"/><rect x="34" y="22" width="16" height="3" fill="#555"/>
        <path d="M42 2 v4 M33 6 l3 3 M51 6 l-3 3 M31 13 h3 M50 13 h3" stroke="#555" stroke-width="1"/>
      </g>
    </svg>
    <p>Serious complications are uncommon after straight forward bariatric procedures however from time to time they will occur. <b><i>Early diagnosis and treatment of complications always leads to best outcomes.</i></b></p>
    <p class="strong" style="margin-top:6px">Things to watch out for…</p>
    <ul class="dots tight" style="margin-top:0">
      <li>Fevers or Sweats that continue unabated</li>
      <li>Measured temperature greater than 38.0 degrees – unabated</li>
      <li>Increasing abdominal pain, unabated</li>
      <li>Difficulties breathing</li>
      <li>Continuous vomiting</li>
      <li>Vomiting blood</li>
    </ul>
    <p>The above issues should trigger you or your carer to contact us.</p>
    <p class="strong" style="margin-top:6px">Important Contact Information</p>
    <ul class="arrows tight" style="margin-top:0">
      <li>If you are feeling extremely sick or vomiting blood call an ambulance.</li>
      <li>If you have less urgent concerns about your condition call the rooms to discuss on 9000 4100</li>
      <li>After hours if you have urgent concerns text (preferred) or call Mr Calder on 0400 111 222 or Ms Priya Grewal (Pia) on 0400 333 444</li>
    </ul>
    <p class="strong" style="margin-top:5px">If you decide to present to a hospital emergency department the following are best options:</p>
    <ul class="dots tight">
      <li><b>Ashgrove Public Hospital.</b>
        <ul class="arrows nested"><li>No cost involved. Occasionally significant waiting times to be seen initially</li></ul></li>
      <li><b>Kingsford Private Hospital</b>
        <ul class="arrows nested"><li>If you have private insurance this may allow you to be seen quicker</li></ul></li>
      <li><b>Other local hospital or regional hospital.</b>
        <ul class="arrows nested"><li>Relevant expertise may not be available hence it is always worth contacting our rooms or Mr Calder or Ms Grewal to let us know you are attending.</li></ul></li>
    </ul>
    <p style="margin-top:4px">Note that it is best to discuss with Mr Calder or Ms Grewal prior to presenting to emergency departments as he can advise the best option given your particular circumstances.</p>
  </div>
  <footer class="page-foot"><span class="num">8</span><span class="text"><b>Calloway Centre for Bariatric Surgery.</b> Post operative instructions for bariatric patients</span></footer>
</section>

</body>
</html>
```